Vietnamese Restaurant Poster

We are a family restaurant specializing in Vietnamese comfort food of pho (Vietnamese Beef Noodle Soup).

We need to create a poster that will attract customers driving by our restaurant.

This poster will be placed on sandwich boards and placed on the intersecting streets.

We want it to be
- big and visually appealing.
- Preferably with a logo incorporating our name and a bowl of Pho
- a arrow sign pointing right
- our phone number 604-318-7915

The name of our restaurant is:

Pho Lanh Tuyet (Title text)
Vietnamese Restaurant (smaller text)

Reason: We have narrowed it down to 2  designs that we absolutely love. Thank you to all who have submitted.

Target Market(s)

Caucasian people who have not tried Vietnamese food. Our location is a little hidden so we want to make these posters to put on the main streets which will grab attention of people driving by to come into our restaurant

Industry/Entity Type

Restaurant

Requirements
Must have
• - big and visually appealing.
logo incorporating our name and a bowl of Pho
Nice to have
• a person eating a bowl of pho

```html
<!DOCTYPE html>
<html lang="en">
<head>
<meta charset="utf-8">
<title>Pho Lanh Tuyet Vietnamese Restaurant Poster</title>
<link rel="stylesheet" href="https://fonts.googleapis.com/css2?family=Bevan&family=Fondamento&family=Arimo:wght@400&family=Alfa+Slab+One&display=swap">
<style>
  :root {
    --sky-top: #f07a12;
    --sky-mid: #f39a2a;
    --sky-low: #e98d2a;
    --ink: #120a04;
    --shade: #1a0c03;
    --cream: #f6e7b0;
    --gold: #f5b428;
    --gold-deep: #e07812;
    --badge-red: #c8261a;
    --badge-gold: #f3c23a;
    --broth: #4a2a12;
    --bowl-rim: #efe9df;
  }
  * { margin: 0; padding: 0; box-sizing: border-box; }
  html, body { width: 850px; height: 1200px; overflow: hidden; background: var(--sky-top); }
  .poster {
    position: relative;
    width: 850px;
    height: 1200px;
    overflow: hidden;
    background: linear-gradient(180deg, var(--sky-top) 0%, var(--sky-mid) 40%, var(--sky-low) 62%, var(--sky-top) 100%);
  }
  .poster-art { position: absolute; inset: 0; }
  .masthead { position: absolute; top: 40px; left: 0; width: 850px; text-align: center; color: var(--ink); font-family: "Bevan", serif; line-height: 1; }
  .masthead-name { font-size: 54px; letter-spacing: 1px; }
  .masthead-cuisine { font-size: 66px; margin-top: 14px; letter-spacing: 1px; }
  .masthead-type { font-size: 36px; margin-top: 6px; }
  .dish { position: absolute; left: 0; width: 850px; text-align: center; line-height: 1; }
  .dish-origin { top: 795px; font-family: "Bevan", serif; font-size: 60px; color: var(--gold); padding-left: 60px; text-shadow: 0 2px 0 var(--gold-deep); }
  .dish-name { top: 868px; font-family: "Fondamento", cursive; font-size: 86px; color: var(--cream); text-shadow: 3px 3px 0 var(--ink); }
  .must-try {
    position: absolute; left: 160px; top: 742px; width: 104px; height: 104px; border-radius: 50%;
    background: var(--badge-red); border: 5px solid var(--badge-gold);
    transform: rotate(-14deg);
    display: flex; flex-direction: column; align-items: center; justify-content: center;
    font-family: "Alfa Slab One", serif; color: var(--badge-gold); font-size: 24px; line-height: 1;
  }
  .call-line {
    position: absolute; left: 118px; top: 1012px; height: 68px;
    display: flex; align-items: center;
    font-family: "Alfa Slab One", serif; font-size: 54px; color: var(--cream); letter-spacing: 1px;
  }
</style>
</head>
<body>
<main class="poster">
  <svg class="poster-art" width="850" height="1200" viewBox="0 0 850 1200" xmlns="http://www.w3.org/2000/svg">
    <defs>
      <radialGradient id="vignette" cx="50%" cy="50%" r="50%">
        <stop offset="0%" stop-color="var(--shade)" stop-opacity="1"/>
        <stop offset="72%" stop-color="var(--shade)" stop-opacity="0.95"/>
        <stop offset="100%" stop-color="var(--shade)" stop-opacity="0"/>
      </radialGradient>
      <linearGradient id="figures" x1="0" y1="0" x2="0" y2="1">
        <stop offset="0%" stop-color="#2a1406"/>
        <stop offset="100%" stop-color="#120802"/>
      </linearGradient>
      <radialGradient id="bowlFill" cx="50%" cy="50%" r="50%">
        <stop offset="0%" stop-color="#7a4a22"/>
        <stop offset="80%" stop-color="var(--broth)"/>
        <stop offset="100%" stop-color="#2b170a"/>
      </radialGradient>
      <path id="bowlArc" d="M 232 700 A 212 212 0 0 1 560 440"/>
    </defs>

    <rect class="horizon-band" x="0" y="640" width="850" height="40" fill="#c8641a" opacity="0.35"/>

    <g role="img" aria-label="Silhouettes of three people in conical hats standing against an orange sky">
      <rect x="130" y="275" width="510" height="330" rx="80" fill="url(#figures)" opacity="0.9"/>
    </g>

    <ellipse class="bowl-vignette" cx="435" cy="690" rx="330" ry="280" fill="url(#vignette)"/>

    <g role="img" aria-label="Bowl of Vietnamese beef noodle soup with beef balls, sliced beef and cilantro">
      <circle cx="442" cy="650" r="186" fill="var(--bowl-rim)"/>
      <circle cx="442" cy="650" r="170" fill="url(#bowlFill)"/>
    </g>

    <text font-family="Arimo, sans-serif" font-size="22" fill="#ffffff" letter-spacing="0.5">
      <textPath href="#bowlArc">specializing in Vietnamese homely comfort food of pho</textPath>
    </text>

    <g class="direction-arrow">
      <polygon points="86,1005 700,1005 700,968 765,1045 700,1122 700,1085 86,1085" fill="var(--ink)"/>
    </g>
  </svg>

  <header class="masthead">
    <div class="masthead-name">Pho Lanh Tuyet</div>
    <div class="masthead-cuisine">Vietnamese</div>
    <div class="masthead-type">Restaurant</div>
  </header>

  <div class="must-try"><span>MUST</span><span>TRY</span></div>
  <div class="dish dish-origin">Vietnamese</div>
  <div class="dish dish-name">Beef Noodle Soup</div>

  <div class="call-line">Call 604-318-7915</div>
</main>
</body>
</html>
```